Business Card for TOV

We need a Corporate style business card for a new Industrial recycling company based in Australia. We recycle industrial products from Mining companies, power stations and other large industry all around the country.

We want the card to represent a modern, innovative professional company that is an industry leader.

We want the card to be double sided. I think with the logo centred by itself on one side and the text displayed with all our details on the other side.

(or you could put the persons name with the job title on the side with the logo?? I'll leave that up to your creative sides)

Open to how you divide and place the information on the one side of the card.

I think the persons name and the title should have its own place. The rest of the information can be placed as you think is best and then I will provide feedback as to what I think works best.

I have attached the logo file so you can add that to the one side. Whether you use it in a smaller form on the second side too is an option but I'll leave that up to you initially?

Information required on the card is as follows

Dermot Halloran
Director

0438 972 506

dermot@tovq.com.au

Po Box 782
Brindle ACT 2694

www.tovq.com.au

ACN 582 917 306 (This can be in very small print and can be in the bottom corner of the card or somewhere not very prominent

Wanted to thank everyone for their submissions. 

We were really torn on about 5 designs in the end.

We decided to go with the first one we liked.

We have another company that is going to need logo and business card design in the coming weeks.

I will save your designer ID's so I can invite you all to that project. too!

Thanks again and all the best

Dermot

Target Market(s)

Corporate and medium to large business clients

Industry/Entity Type

Industrial

```html
<!DOCTYPE html>
<html lang="en">
<head>
<meta charset="utf-8">
<title>TOV Resource Group – Business Card</title>
<link href="https://fonts.googleapis.com/css2?family=Open+Sans:wght@400;600;700&family=Roboto+Condensed:wght@400;700&display=swap" rel="stylesheet">
<style>
  :root {
    --bg: #e6e6e4;
    --card: #ffffff;
    --card-back-top: #ffffff;
    --card-back-bottom: #e4e4e4;
    --green: #4aa32e;
    --green-light: #6cc04a;
    --ink: #333333;
    --ink-soft: #555555;
    --rule: #b9b9b9;
  }
  * { box-sizing: border-box; margin: 0; padding: 0; }
  html, body {
    width: 1200px; height: 1024px; overflow: hidden;
    background: var(--bg);
    font-family: "Open Sans", Arial, sans-serif;
  }
  .canvas {
    width: 1200px; height: 1024px;
    display: flex; flex-direction: column; align-items: center; justify-content: center;
    gap: 70px;
  }
  .card {
    position: relative;
    width: 760px; height: 430px;
    background: var(--card);
    box-shadow: 0 6px 18px rgba(0,0,0,.18);
    overflow: hidden;
  }
  .card-band {
    position: absolute; left: 0; right: 0; bottom: 0; height: 30px;
    background: linear-gradient(90deg, var(--green) 0%, var(--green-light) 100%);
  }

  /* Front */
  .brand {
    position: absolute; left: 44px; top: 72px;
    display: flex; align-items: center; gap: 18px;
  }
  .brand-mark {
    width: 64px; height: 64px; border-radius: 50%;
    background: var(--green);
    flex: none;
  }
  .brand-name {
    font-family: "Open Sans", Arial, sans-serif;
    font-weight: 700; color: var(--ink);
    font-size: 24px; line-height: 1.15; letter-spacing: .5px;
    text-transform: uppercase; white-space: nowrap;
  }
  .person {
    position: absolute; right: 70px; top: 62px; text-align: left;
  }
  .person-name {
    font-family: "Roboto Condensed", Arial, sans-serif;
    font-size: 30px; color: var(--green); font-weight: 400; line-height: 1.1;
  }
  .person-title {
    font-size: 11px; color: var(--ink); letter-spacing: .5px; margin-top: 4px;
  }
  .divider {
    position: absolute; left: 44px; right: 40px; top: 180px;
    height: 1px; background: var(--rule);
  }
  .contacts {
    position: absolute; left: 44px; top: 210px; list-style: none;
  }
  .contact {
    display: flex; align-items: center; gap: 18px;
    font-size: 16px; color: var(--ink-soft); height: 35px;
  }
  .contact-icon { width: 20px; height: 20px; flex: none; }
  .acn {
    position: absolute; right: 40px; bottom: 48px;
    font-size: 10px; color: var(--ink); letter-spacing: .3px;
  }

  /* Back */
  .card-back {
    background: radial-gradient(ellipse at 50% 40%, var(--card-back-top) 0%, var(--card-back-bottom) 100%);
  }
  .back-brand {
    position: absolute; left: 0; right: 0; top: 0; bottom: 30px;
    display: flex; align-items: center; justify-content: center; gap: 26px;
  }
  .back-brand .brand-mark { width: 100px; height: 100px; }
  .back-brand .brand-name { font-size: 40px; }
</style>
</head>
<body>
<main class="canvas">

  <section class="card card-front" aria-label="Card front">
    <div class="brand">
      <span class="brand-mark"></span>
      <span class="brand-name">TOV Resource Group</span>
    </div>

    <div class="person">
      <div class="person-name">Dermot Halloran</div>
      <div class="person-title">DIRECTOR</div>
    </div>

    <div class="divider"></div>

    <ul class="contacts">
      <li class="contact">
        <svg class="contact-icon" viewBox="0 0 20 20" aria-hidden="true">
          <path d="M5 2.5c.8-.5 1.6-.3 2 .4l1.5 2.6c.4.7.2 1.4-.4 1.8l-1 .7c.6 1.8 2 3.4 3.9 4.4l.8-1c.5-.6 1.2-.7 1.8-.3l2.5 1.7c.7.4.8 1.3.3 2l-1 1.2c-.9 1-2.5 1.2-4 .5C7.3 14.6 4.6 11.3 3.5 7.6 3 6 3.3 4.3 4.3 3.2z" fill="var(--green)"/>
        </svg>
        0438 972 506
      </li>
      <li class="contact">
        <svg class="contact-icon" viewBox="0 0 20 20" aria-hidden="true">
          <circle cx="10" cy="10" r="9.5" fill="var(--green)"/>
          <rect x="5" y="6.5" width="10" height="7" rx="1" fill="#fff"/>
          <path d="M5.5 7l4.5 3.6L14.5 7" fill="none" stroke="var(--green)" stroke-width="1.2"/>
        </svg>
        dermot@tovq.com.au
      </li>
      <li class="contact">
        <svg class="contact-icon" viewBox="0 0 20 20" aria-hidden="true">
          <circle cx="10" cy="10" r="9.5" fill="var(--green)"/>
          <g fill="none" stroke="#fff" stroke-width="1.1">
            <circle cx="10" cy="10" r="5.5"/>
            <ellipse cx="10" cy="10" rx="2.4" ry="5.5"/>
            <line x1="4.5" y1="10" x2="15.5" y2="10"/>
          </g>
        </svg>
        www.tovq.com.au
      </li>
      <li class="contact">
        <svg class="contact-icon" viewBox="0 0 20 20" aria-hidden="true">
          <circle cx="10" cy="10" r="9.5" fill="var(--green)"/>
          <path d="M10 4.5a3.5 3.5 0 0 1 3.5 3.5c0 2.6-3.5 7-3.5 7s-3.5-4.4-3.5-7A3.5 3.5 0 0 1 10 4.5z" fill="#fff"/>
          <circle cx="10" cy="8" r="1.3" fill="var(--green)"/>
        </svg>
        Po Box 782, Brindle ACT 2694
      </li>
    </ul>

    <div class="acn">ACN 582 917 306</div>
    <div class="card-band"></div>
  </section>

  <section class="card card-back" aria-label="Card back">
    <div class="back-brand">
      <span class="brand-mark"></span>
      <span class="brand-name">TOV Resource Group</span>
    </div>
    <div class="card-band"></div>
  </section>

</main>
</body>
</html>
```